BRISK GUARD WEBSITE BANNER DESIGN OF AWESOME

Please take a look at the attached Banner. I want a redesign Idea. The requirements are below.

1)Must Use Website Background
2)Must Use Photo Provided
3)Must Include Button
4)Website the banner will be used on you can see the current at the bottom of the page: https://b.plomvarn.com

Target Market(s)

Anyone Seeking Security Guard Services

```html
<!DOCTYPE html>
<html lang="en">
<head>
<meta charset="UTF-8">
<title>Brisk Guard – Website Banner</title>
<link rel="stylesheet" href="https://fonts.googleapis.com/css2?family=Poppins:wght@400;500;600;700&display=swap">
<style>
  :root {
    --page-bg: #f9f4b0;
    --navy: #17365c;
    --steel-blue: #1a4f7c;
    --gold: #fbab18;
    --gold-light: #fde7a8;
    --white: #ffffff;
    --photo-dark: #101c30;
    --photo-mid: #2a4a78;
    --photo-light: #7f9cc8;
  }
  * { margin: 0; padding: 0; box-sizing: border-box; }
  html, body {
    width: 1200px;
    height: 960px;
    overflow: hidden;
    background: var(--page-bg);
    font-family: "Poppins", sans-serif;
  }
  .banner {
    position: absolute;
    left: 41px;
    top: 391px;
    width: 1119px;
    height: 233px;
    overflow: hidden;
    box-shadow: 0 3px 8px rgba(0, 0, 0, 0.35);
  }
  .banner-shapes {
    position: absolute;
    inset: 0;
  }
  .headline {
    position: absolute;
    left: 0;
    width: 768px;
    top: 9px;
    text-align: center;
    font-weight: 700;
    font-size: 41px;
    letter-spacing: 2px;
    line-height: 50px;
    background: linear-gradient(180deg, var(--gold-light) 0%, var(--gold) 85%);
    -webkit-background-clip: text;
    background-clip: text;
    color: transparent;
  }
  .tagline {
    position: absolute;
    left: 0;
    width: 768px;
    top: 62px;
    text-align: center;
    font-weight: 400;
    font-size: 20px;
    letter-spacing: 1px;
    color: var(--white);
  }
  .feature {
    position: absolute;
    top: 107px;
    height: 39px;
    display: flex;
    align-items: center;
    gap: 10px;
    color: var(--white);
    font-weight: 500;
    font-size: 18px;
    letter-spacing: 1px;
    white-space: nowrap;
  }
  .feature-icon {
    width: 39px;
    height: 39px;
    border-radius: 50%;
    background: var(--white);
    display: flex;
    align-items: center;
    justify-content: center;
    flex: none;
  }
  .feature-client { left: 30px; }
  .feature-dispatch { left: 230px; }
  .feature-contracts { left: 432px; }
  .cta-button {
    position: absolute;
    left: 279px;
    top: 177px;
    width: 207px;
    height: 44px;
    border-radius: 22px;
    background: var(--gold);
    color: var(--navy);
    font-weight: 600;
    font-size: 21px;
    letter-spacing: 1px;
    display: flex;
    align-items: center;
    justify-content: center;
    gap: 14px;
    text-decoration: none;
  }
  .brand-name {
    position: absolute;
    left: 988px;
    top: 34px;
    font-weight: 600;
    font-size: 15px;
    letter-spacing: 1px;
    color: var(--white);
  }
</style>
</head>
<body>
  <section class="banner">
    <svg class="banner-shapes" width="1119" height="233" viewBox="0 0 1119 233" xmlns="http://www.w3.org/2000/svg">
      <defs>
        <linearGradient id="photoTone" x1="0" y1="1" x2="1" y2="0">
          <stop offset="0" stop-color="var(--photo-dark)"/>
          <stop offset="0.55" stop-color="var(--photo-mid)"/>
          <stop offset="1" stop-color="var(--photo-light)"/>
        </linearGradient>
      </defs>
      <rect class="base" width="1119" height="233" fill="var(--navy)"/>
      <polygon class="accent-left" points="0,0 174,233 0,233" fill="var(--steel-blue)"/>
      <polygon class="accent-right" points="611,0 819,0 700,119" fill="var(--steel-blue)"/>
      <polygon class="chevron" points="819,0 833,0 717,119 811,233 797,233 700,119" fill="var(--gold)"/>
      <polygon class="photo-area" role="img" aria-label="Photo: security guard in a dark jacket shining a flashlight up a stairwell" points="833,0 1119,0 1119,233 811,233 717,119" fill="url(#photoTone)"/>
    </svg>

    <h1 class="headline">GET SECURED TODAY</h1>
    <p class="tagline">We take your security personal</p>

    <div class="feature feature-client">
      <span class="feature-icon">
        <svg width="24" height="20" viewBox="0 0 24 20" fill="var(--navy)">
          <circle cx="12" cy="4" r="3.5"/><circle cx="4.5" cy="6" r="2.5"/><circle cx="19.5" cy="6" r="2.5"/>
          <path d="M6.5 19v-5a5.5 5.5 0 0 1 11 0v5z"/><path d="M0.5 19v-4a4 4 0 0 1 5-3.8V19z"/><path d="M23.5 19v-4a4 4 0 0 0-5-3.8V19z"/>
        </svg>
      </span>
      Client portal
    </div>

    <div class="feature feature-dispatch">
      <span class="feature-icon">
        <svg width="26" height="26" viewBox="0 0 26 26" fill="none" stroke="var(--navy)" stroke-width="2">
          <circle cx="12" cy="12" r="10"/>
          <path d="M12 6v6l-3 3"/>
          <text x="13" y="24" font-family="Poppins, sans-serif" font-size="9" font-weight="700" fill="var(--navy)" stroke="none">24</text>
        </svg>
      </span>
      24X7 Dispatch
    </div>

    <div class="feature feature-contracts">
      <span class="feature-icon">
        <svg width="26" height="18" viewBox="0 0 26 18" fill="var(--navy)">
          <path d="M0 3h5l2 9H2z"/><path d="M26 3h-5l-2 9h5z"/>
          <path d="M6 4l6-2 3 2 5-1 1 8-5 5-3-1-7-4z"/>
        </svg>
      </span>
      No Binding Contracts
    </div>

    <a class="cta-button" href="#">Get Started
      <svg width="11" height="14" viewBox="0 0 11 14"><path d="M2 2l6 5-6 5" fill="none" stroke="var(--navy)" stroke-width="3" stroke-linecap="round" stroke-linejoin="round"/></svg>
    </a>

    <span class="brand-name">BRISK GUARD</span>
  </section>
</body>
</html>
```